Marist District College Brenthollow Letterhead

Our college is called Marist District College Brenthollow. We would like to request a few letterhead design options to choose from please. We look forward to seeing some new and fresh ideas for our College Letterhead.

Please note that the College has the following PMS Colours:
MAROON – PMS 229C
BLUE – PMS 2747C
GOLD – PMS 871C
YELLOW – PMS 123C

Our College Motto is:
Light guiding Purpose.
I have attached a copy of our current letterhead and College Logo.

Please note that the letterhead must include the following details:

Marist District College Brenthollow
Light Guiding Purpose
Phone: 9472 0000
Fax:9481 3157
Address: 517 Brenthollow Road Brenthollow 3037
Mail:PO BOX 4817 Wattle Bend VIC 3038 Australia
ABN 47 816 205 938

www.mdcbrenthollow-example.net
https://twitter.com/mdcbrenthollow
https://www.pinterest.com/mdcbrenthollow
https://www.facebook.com/MDCBrenthollow
www.tubecast-example.com (search MDC Brenthollow)

Please feel free to contact me on the below detail if I can further assist.

Regards,
Joanna Verkuil
reception@mdcbrenthollow-example.net
PH: 9472 0000

Target Market(s)

College Community

Industry/Entity Type

Education

Requirements
Must have
• See Project Description
Nice to have
• see Project Description

```html
<!DOCTYPE html>
<html lang="en">
<head>
<meta charset="utf-8">
<title>Marist District College Brenthollow – Letterhead Options</title>
<link href="https://fonts.googleapis.com/css2?family=Ubuntu:wght@400;500;700&display=swap" rel="stylesheet">
<style>
  :root {
    --maroon: #8b1f3a;
    --blue: #1f2f5c;
    --gold: #b58b2a;
    --yellow: #ffcc14;
    --paper: #ffffff;
    --ink: #555a60;
    --backdrop: #ece9e6;
    --ghost: #f5f7f9;
  }
  * { margin: 0; padding: 0; box-sizing: border-box; }
  html, body { width: 1200px; height: 1000px; overflow: hidden; }
  body {
    background: var(--backdrop);
    font-family: "Ubuntu", "Helvetica Neue", Arial, sans-serif;
    position: relative;
  }
  .letterhead {
    position: absolute;
    top: 177px;
    width: 474px;
    height: 614px;
    background: var(--paper);
    box-shadow: 0 6px 18px rgba(0,0,0,0.18);
    overflow: hidden;
  }
  .letterhead--plain { left: 86px; }
  .letterhead--accent { left: 661px; }

  .header-art { position: absolute; left: 0; top: 0; width: 474px; height: 190px; }

  .motto {
    position: absolute; left: 21px; top: 22px;
    color: #fff; font-weight: 700; font-size: 13.5px; letter-spacing: 0.1px;
  }
  .motto .highlight { color: var(--yellow); }
  .header-divider {
    position: absolute; left: 218px; top: 21px; width: 1px; height: 20px;
    background: #e6c9d0;
  }
  .college-name {
    position: absolute; right: 22px; top: 23px;
    color: var(--yellow); font-weight: 500; font-size: 12.5px;
  }
  .college-contact {
    position: absolute; right: 23px; top: 43px;
    color: #fff; font-size: 8px; font-weight: 500;
  }
  .college-contact .label { color: var(--yellow); }

  .crest {
    position: absolute; left: 315px; top: 74px; width: 104px; height: 104px;
    border-radius: 50%; background: var(--paper);
    display: flex; align-items: center; justify-content: center; text-align: center;
    color: var(--maroon); font-weight: 700; font-size: 10px; line-height: 1.25;
    padding: 14px;
  }

  .ghost-circle { position: absolute; border-radius: 50%; background: var(--ghost); }
  .ghost-circle--upper { left: 195px; top: 195px; width: 162px; height: 162px; }
  .ghost-circle--lower { left: 37px; top: 353px; width: 220px; height: 220px; }

  .footer-bar-left {
    position: absolute; left: 0; top: 547px; width: 15px; height: 48px;
    background: var(--yellow);
  }
  .footer-bar-right {
    position: absolute; right: 0; top: 548px; width: 16px; height: 47px;
    background: var(--maroon);
  }
  .footer-divider {
    position: absolute; left: 203px; top: 548px; width: 1px; height: 47px;
    background: var(--maroon);
  }
  .footer-address, .footer-links {
    position: absolute; top: 550px; font-size: 7px; line-height: 9.3px;
    color: var(--ink); font-style: normal; font-weight: 400; white-space: nowrap;
  }
  .footer-address { left: 25px; }
  .footer-links { right: 26px; text-align: right; }
  .footer-address .label, .footer-address .abn, .footer-links .brand { color: var(--maroon); }
</style>
</head>
<body>

<article class="letterhead letterhead--plain">
  <svg class="header-art" viewBox="0 0 474 190" aria-hidden="true">
    <polygon points="0,0 474,0 474,72 362,117 0,58" fill="var(--maroon)"/>
    <polygon points="0,58 362,117 474,72 474,79 362,125 0,65" fill="var(--yellow)"/>
  </svg>
  <p class="motto">Light <span class="highlight">Guiding</span> Purpose</p>
  <span class="header-divider"></span>
  <p class="college-name">Marist District College Brenthollow</p>
  <p class="college-contact"><span class="label">Phone</span> : 9472 0000 | <span class="label">Fax</span> : 9481 3157</p>
  <div class="crest">Marist District College Brenthollow</div>

  <span class="footer-bar-left"></span>
  <address class="footer-address">
    <span class="label">Address</span> : 517 Brenthollow Road<br>
    Brenthollow 3094<br>
    <span class="label">Mail</span> : PO BOX 4817 Wattle Bend<br>
    VIC 3097 Australia<br>
    <span class="abn">ABN 47 816 205 938</span>
  </address>
  <span class="footer-divider"></span>
  <div class="footer-links">
    www.<span class="brand">mdcbrenthollow-example</span>.net<br>
    https://<span class="brand">chirpline-example</span>.com/mdcbrenthollow<br>
    https://www.<span class="brand">pinboard-example</span>.com/mdcbrenthollow<br>
    https://www.<span class="brand">friendspace-example</span>.com/MDCBrenthollow<br>
    www.<span class="brand">tubecast-example</span>.com (search MDC Brenthollow)
  </div>
  <span class="footer-bar-right"></span>
</article>

<article class="letterhead letterhead--accent">
  <span class="ghost-circle ghost-circle--upper"></span>
  <span class="ghost-circle ghost-circle--lower"></span>
  <svg class="header-art" viewBox="0 0 474 190" aria-hidden="true">
    <polygon points="0,0 474,0 474,72 362,117 0,58" fill="var(--maroon)"/>
    <polygon points="0,58 362,117 474,72 474,79 362,125 0,65" fill="var(--yellow)"/>
  </svg>
  <p class="motto">Light <span class="highlight">Guiding</span> Purpose</p>
  <span class="header-divider"></span>
  <p class="college-name">Marist District College Brenthollow</p>
  <p class="college-contact"><span class="label">Phone</span> : 9472 0000 | <span class="label">Fax</span> : 9481 3157</p>
  <div class="crest">Marist District College Brenthollow</div>

  <span class="footer-bar-left"></span>
  <address class="footer-address">
    <span class="label">Address</span> : 517 Brenthollow Road<br>
    Brenthollow 3094<br>
    <span class="label">Mail</span> : PO BOX 4817 Wattle Bend<br>
    VIC 3097 Australia<br>
    <span class="abn">ABN 47 816 205 938</span>
  </address>
  <span class="footer-divider"></span>
  <div class="footer-links">
    www.<span class="brand">mdcbrenthollow-example</span>.net<br>
    https://<span class="brand">chirpline-example</span>.com/mdcbrenthollow<br>
    https://www.<span class="brand">pinboard-example</span>.com/mdcbrenthollow<br>
    https://www.<span class="brand">friendspace-example</span>.com/MDCBrenthollow<br>
    www.<span class="brand">tubecast-example</span>.com (search MDC Brenthollow)
  </div>
  <span class="footer-bar-right"></span>
</article>

</body>
</html>
```